Flyer to Promote Membership in a Trade Association

UPDATE: I am looking for something modern and clean. NO CLIP ART. Not flashy. Just professional and modern. For everyone looking at our current flyer, we don't like it. That's why we aer looking for a new one. So please don't replicate it or use it as inspiration.

I need a flyer to promote membership in the Durable Residence Backers League. It can (probably should) be 2-sided. The content is attached as well as our logo and brand guidelines.

```html
<!DOCTYPE html>
<html lang="en">
<head>
<meta charset="utf-8">
<title>Durable Residence Backers League – Membership Flyer</title>
<link href="https://fonts.googleapis.com/css2?family=Montserrat:wght@400;500;600;700;800&display=swap" rel="stylesheet">
<style>
  :root {
    --orange: #f27a2e;
    --band-dark: #474b51;
    --band-footer: #6b7077;
    --ink: #3c3f44;
    --ink-soft: #5d6168;
    --rule: #7a7e85;
    --paper: #ffffff;
    --backdrop: #d9d9d9;
  }
  * { margin: 0; padding: 0; box-sizing: border-box; }
  html, body { width: 1200px; height: 1200px; overflow: hidden; }
  body {
    background: var(--backdrop);
    font-family: "Montserrat", Arial, sans-serif;
    position: relative;
  }
  .sheet-slot { position: absolute; top: 232px; width: 520px; height: 735px; }
  .sheet-slot.back { left: 60px; }
  .sheet-slot.front { left: 620px; }
  .sheet {
    position: absolute; top: 0; left: 0;
    width: 480px; height: 678px;
    background: var(--paper);
    transform: scale(1.0833);
    transform-origin: top left;
    overflow: hidden;
    box-shadow: 0 10px 24px rgba(0,0,0,0.18);
  }
  .chevron { position: absolute; top: 0; left: 0; width: 480px; height: 287px; }

  .brand {
    position: absolute; top: 15px; left: 22px;
    display: flex; align-items: center; gap: 6px;
    color: var(--ink-soft); font-weight: 700;
  }
  .brand-square { width: 13px; height: 13px; background: var(--orange); }
  .brand-name { font-size: 17px; letter-spacing: -0.3px; }
  .brand-full { font-size: 4.2px; line-height: 1.25; width: 50px; text-transform: uppercase; margin-left: 2px; }

  .photo {
    position: absolute;
    border-radius: 50%;
    border: 5px solid var(--orange);
    background: radial-gradient(circle at 45% 40%, #e9ecee 0%, #b8bec3 55%, #7d868c 100%);
    box-shadow: 0 3px 8px rgba(0,0,0,0.25);
  }
  .back .photo { left: 103px; top: 28px; width: 234px; height: 234px; }
  .front .photo { left: 176px; top: 27px; width: 256px; height: 256px; }

  /* back side */
  .benefits-title {
    position: absolute; left: 31px; top: 267px;
    color: var(--orange); font-size: 11.5px; font-weight: 500; letter-spacing: 0.2px;
  }
  .benefits-band {
    position: absolute; left: 0; top: 287px; width: 480px; height: 217px;
    background: var(--band-dark); color: #fff; padding: 10px 40px 0 31px;
  }
  .benefit { margin-bottom: 9px; }
  .benefit h3 { font-size: 6px; font-weight: 700; text-transform: uppercase; line-height: 1.3; }
  .benefit p { font-size: 6px; line-height: 1.35; font-weight: 400; }

  .cta {
    position: absolute; left: 50%; transform: translateX(-50%);
    display: flex; flex-direction: column; align-items: center;
  }
  .back .cta { top: 514px; }
  .front .cta { top: 522px; }
  .cta-button {
    display: flex; align-items: center; gap: 6px;
    background: var(--orange); color: #fff;
    height: 35px; padding: 0 16px 0 17px; border-radius: 18px;
    font-size: 18.5px; font-weight: 700; letter-spacing: 0.2px; white-space: nowrap;
  }
  .cta-button svg { width: 17px; height: 17px; }
  .cta-url { font-size: 15px; color: var(--ink); margin-top: 2px; font-weight: 500; }

  .members {
    position: absolute; left: 0; bottom: 0; width: 480px; height: 89px;
    background: var(--band-footer); color: #fff; padding: 8px 22px 0 23px;
    font-size: 5.8px; line-height: 1.55;
  }

  /* front side */
  .headline {
    position: absolute; left: 22px; top: 60px; width: 152px;
    color: var(--orange); font-size: 12.8px; font-weight: 700; line-height: 1.25;
  }
  .intro {
    position: absolute; left: 23px; top: 172px; width: 142px;
    color: var(--ink-soft); font-size: 7px; line-height: 1.4;
  }
  .stats {
    position: absolute; left: 0; top: 289px; width: 480px; height: 62px;
    background: var(--orange); display: flex; align-items: center;
  }
  .stat {
    flex: 1; text-align: center; color: #fff; font-weight: 700;
    font-size: 9px; line-height: 1.3; text-transform: uppercase;
    border-right: 1px solid rgba(255,255,255,0.45); height: 42px;
    display: flex; align-items: center; justify-content: center;
  }
  .stat:last-child { border-right: none; }
  .columns { position: absolute; top: 361px; left: 23px; width: 440px; display: flex; align-items: flex-start; }
  .column h2 { font-size: 8.4px; font-weight: 700; color: var(--ink); margin-bottom: 4px; text-transform: uppercase; }
  .column ul { list-style: none; }
  .column li {
    font-size: 6.4px; color: var(--ink-soft); line-height: 1.75;
    display: flex; align-items: center; gap: 4px; white-space: nowrap;
  }
  .column li::before {
    content: ""; width: 4px; height: 4px; border-radius: 50%;
    border: 1.2px solid var(--ink); flex: none;
  }
  .column.activities { width: 202px; }
  .column.pricing { padding-left: 28px; }
  .column-rule { width: 1px; height: 76px; background: var(--rule); margin-top: 10px; }
  .access-box {
    position: absolute; left: 59px; top: 468px; width: 362px; height: 40px;
    border: 2px solid var(--ink-soft); color: var(--ink-soft);
    display: flex; flex-direction: column; justify-content: center; align-items: center;
    font-size: 8.2px; font-weight: 600; line-height: 1.3; text-transform: uppercase;
  }
</style>
</head>
<body>

<div class="sheet-slot back">
  <section class="sheet">
    <svg class="chevron" viewBox="0 0 480 287" aria-hidden="true">
      <polygon fill="var(--orange)" points="390,0 480,0 480,55 390,143 480,231 480,287 390,287 245,143"/>
    </svg>
    <div class="brand">
      <span class="brand-square"></span>
      <span class="brand-name">DRBL</span>
      <span class="brand-full">Durable Residence Backers League</span>
    </div>
    <div class="photo" role="img" aria-label="Photo of three professionals shaking hands beside an architectural building model"></div>
    <h2 class="benefits-title">MEMBER BENEFITS</h2>
    <div class="benefits-band">
      <div class="benefit"><h3>Members-Only Conferences</h3><p>Two annual in-person meetings. Spring Meeting: investors-only for candid peer conversations. Fall Summit: full ecosystem gathering with syndicators and brokers.</p></div>
      <div class="benefit"><h3>Investor-Only Forums</h3><p>Exclusive meetings and webinars for investors only, enabling candid conversations and meaningful collaboration.</p></div>
      <div class="benefit"><h3>Peer-to-Peer Meetups</h3><p>Find your peers—underwriters, asset managers, credit officers and more—with our meetups.</p></div>
      <div class="benefit"><h3>Live &amp; On-Demand Webinars</h3><p>Free monthly Third Thursday webinars covering Year 15 issues, secondary transactions, securitizing developer fees and other emerging topics.</p></div>
      <div class="benefit"><h3>Searchable Member Directory</h3><p>Find underwriters, asset managers, and credit officers—searchable by role, firm type, and investment approach.</p></div>
      <div class="benefit"><h3>Shape Industry Standards &nbsp;[Investor Only]</h3><p>DRBL's underwriting and asset management standards are adopted industry-wide. Influence them through our committees.</p></div>
      <div class="benefit"><h3>Emerging Leaders Program &nbsp;[Investor Only]</h3><p>Develop your firm's next-generation leaders through dedicated professional development programming.</p></div>
    </div>
    <div class="cta">
      <div class="cta-button">
        <svg viewBox="0 0 20 20" aria-hidden="true"><circle cx="10" cy="10" r="10" fill="#fff"/><polyline points="8,5.5 12.5,10 8,14.5" fill="none" stroke="var(--orange)" stroke-width="2.6" stroke-linecap="round" stroke-linejoin="round"/></svg>
        READY TO JOIN?
      </div>
      <div class="cta-url">drbl.org</div>
    </div>
    <footer class="members">
      Our Investor Members Include<br>
      Halvane Health · Quarrow Bank · Ostrane Trust Bank · Bank of Northvale · Dravena Bank · Brantley Vail Financial ·
      Capital Summit · Larkspur Savings Bank · Eastmere Bank · Third Street CDC · Foremost Citizens Bank · Gorsett Partners · Kellowan Trust · Morrow
      Hale · Ambrell Mutual Insurance · New Harbor Life · Northpine (TRA) · Pinecrest Real Estate · Ridgeline Affordable Housing ·
      Corvessa Bank · Sherwood Coatings · Lunstead Bank · Tavrel Bank · Trueway Community Capital · Uplands Bank USA · Veterans Mutual ·
      Union Impact Finance · Velmora Bank
    </footer>
  </section>
</div>

<div class="sheet-slot front">
  <section class="sheet">
    <svg class="chevron" viewBox="0 0 480 287" aria-hidden="true">
      <polygon fill="var(--orange)" points="390,0 480,0 480,55 390,143 480,231 480,287 390,287 245,143"/>
    </svg>
    <div class="brand">
      <span class="brand-square"></span>
      <span class="brand-name">DRBL</span>
      <span class="brand-full">Durable Residence Backers League</span>
    </div>
    <h1 class="headline">Where LIHTC Investing Excellence Begins The Only Community Built Exclusively for Investors</h1>
    <p class="intro">DRBL is where federal housing credit investors connect, learn, and lead. We are the only organization solely dedicated to LIHTC investors—giving you a trusted peer network, industry-setting standards, and the insights to stay informed.</p>
    <div class="photo" role="img" aria-label="Photo of three professionals shaking hands beside an architectural building model"></div>
    <div class="stats">
      <div class="stat">30 Years<br>of Impact</div>
      <div class="stat">60+ Investor<br>Firms</div>
      <div class="stat">1,000+<br>Industry<br>Professionals</div>
    </div>
    <div class="columns">
      <div class="column activities">
        <h2>What Members Do</h2>
        <ul>
          <li>Network: Peer Groups &amp; Forums</li>
          <li>Learn: Conferences &amp; Webinars</li>
          <li>Share: Candid Investor Exchange</li>
          <li>Shape: Standards &amp; Best Practices</li>
          <li>Grow: Professional Development</li>
        </ul>
      </div>
      <div class="column-rule"></div>
      <div class="column pricing">
        <h2>Join DRBL Today</h2>
        <ul>
          <li>Investor Members</li>
          <li>Banks, Insurance Companies, Economic Investors</li>
          <li>$5,000/year (assets ≥$5B)</li>
          <li>$1,000/year (assets &lt;$5B)</li>
          <li>Affiliate Members</li>
          <li>Syndicators &amp; Brokers</li>
          <li>$4,500/year</li>
        </ul>
      </div>
    </div>
    <div class="access-box">
      <span>One membership, unlimited access.</span>
      <span>Your entire team can participate in DRBL activities.</span>
    </div>
    <div class="cta">
      <div class="cta-button">
        <svg viewBox="0 0 20 20" aria-hidden="true"><circle cx="10" cy="10" r="10" fill="#fff"/><polyline points="8,5.5 12.5,10 8,14.5" fill="none" stroke="var(--orange)" stroke-width="2.6" stroke-linecap="round" stroke-linejoin="round"/></svg>
        READY TO JOIN?
      </div>
      <div class="cta-url">drbl.org</div>
    </div>
    <footer class="members">
      Our Investor Members Include<br>
      Halvane Health · Quarrow Bank · Ostrane Trust Bank · Bank of Northvale · Dravena Bank · Brantley Vail Financial ·
      Capital Summit · Larkspur Savings Bank · Eastmere Bank · Third Street CDC · Foremost Citizens Bank · Gorsett Partners · Kellowan Trust · Morrow
      Hale · Ambrell Mutual Insurance · New Harbor Life · Northpine (TRA) · Pinecrest Real Estate · Ridgeline Affordable Housing ·
      Corvessa Bank · Sherwood Coatings · Lunstead Bank · Tavrel Bank · Trueway Community Capital · Uplands Bank USA · Veterans Mutual ·
      Union Impact Finance · Velmora Bank
    </footer>
  </section>
</div>

</body>
</html>
```